BRIXLEY ELECTRICAL

all black background with silver and lime writing, fonts i like are gothic style but am open to ideas, will need a picture logo aswell as im putting this on my van.i am a electrical contractor starting up my own electrical business. underneath brixley electrical heading on card we could put" professiona cost effective soloutions to all your electrical needs".{ or something of that nature }.on aback of card on top half list servises provided, real estate and commercial maintenance, new home and renovation rewires and upgrades, split system air conditioning, floor heat, tv phone data, smoke detoctors, lighting systems , builders welcome, , and also a thankyou for your business.

Industry/Entity Type

Real Estate

Contact Information for Business Card

GAVIN PRESTWORTH
brixleyelectrical@quillnet.com.au
0417352940
lic no 81926
ac lic no l593721
abn 37216405813

```html
<!DOCTYPE html>
<html lang="en">
<head>
<meta charset="utf-8">
<title>Brixley Electrical – Business Card</title>
<link rel="stylesheet" href="https://fonts.googleapis.com/css2?family=Cinzel:wght@700&family=Montserrat:ital,wght@0,300;0,400;1,700&family=Archivo+Black&display=swap">
<style>
  :root {
    --page: #e4e4e2;
    --card-black: #0b0b0b;
    --card-charcoal: #2a2a2a;
    --lime: #1f9a3a;
    --lime-bright: #2fb64b;
    --lime-deep: #0f5a22;
    --silver: #e6e6e6;
    --silver-soft: #bdbdbd;
    --ink: #050505;
  }
  * { box-sizing: border-box; margin: 0; padding: 0; }
  html, body { width: 1200px; height: 900px; overflow: hidden; background: var(--page); }
  .canvas { position: relative; width: 1200px; height: 900px; }

  .card {
    position: absolute; left: 250px; width: 700px; height: 400px;
    overflow: hidden; border-radius: 4px;
    box-shadow: 0 10px 28px rgba(0,0,0,.35);
  }
  .card--back { top: 35px; background: var(--card-black); }
  .card--front {
    top: 465px;
    background: radial-gradient(ellipse at 45% 35%, var(--card-charcoal) 0%, #151515 55%, var(--card-black) 100%);
  }

  /* back */
  .back-bands { position: absolute; inset: 0; }
  .services-heading {
    position: absolute; left: 30px; top: 28px;
    font-family: "Archivo Black", "Arial Black", sans-serif;
    font-weight: 400; color: var(--ink); line-height: .95;
  }
  .services-heading .word { display: block; font-size: 38px; white-space: nowrap; }
  .services-heading .word--second { margin-left: 44px; }
  .services-heading .initial { font-size: 76px; }
  .services-list {
    position: absolute; left: 365px; top: 95px; width: 290px;
    font-family: "Montserrat", sans-serif; font-weight: 400;
    font-size: 16px; line-height: 1.65; color: var(--silver);
  }

  /* front */
  .brand-square {
    position: absolute; left: 44px; top: 96px;
    width: 104px; height: 104px; border-radius: 16px;
    background: linear-gradient(160deg, var(--lime-bright), var(--lime) 60%, var(--lime-deep));
    box-shadow: inset 0 0 0 4px rgba(0,0,0,.25);
  }
  .brand-name {
    position: absolute; left: 170px; top: 88px;
    font-family: "Cinzel", serif; font-weight: 700; color: var(--silver);
    line-height: 1;
  }
  .brand-name .line-main { display: block; font-size: 58px; letter-spacing: .02em; }
  .brand-name .line-sub { display: block; font-size: 21px; letter-spacing: .5em; margin-top: 4px; }
  .brand-rule {
    position: absolute; left: 170px; top: 181px; width: 500px; height: 2px;
    background: linear-gradient(90deg, var(--silver), var(--silver-soft));
  }
  .tagline {
    position: absolute; left: 170px; top: 189px;
    font-family: "Montserrat", sans-serif; font-style: italic; font-weight: 700;
    font-size: 13.5px; color: var(--silver); white-space: nowrap;
  }
  .contact {
    position: absolute; left: 372px; top: 262px;
    font-family: "Montserrat", sans-serif; font-weight: 300; font-style: normal;
    color: var(--silver); line-height: 1.3;
  }
  .contact .person { font-size: 24px; }
  .contact .licences { font-size: 10px; color: var(--silver-soft); letter-spacing: .03em; margin-bottom: 4px; }
  .contact .phone { font-size: 21px; }
  .contact .email { font-size: 18px; }
</style>
</head>
<body>
<main class="canvas">

  <section class="card card--back" aria-label="Business card back">
    <svg class="back-bands" width="700" height="400" viewBox="0 0 700 400" aria-hidden="true">
      <defs>
        <linearGradient id="band-green" x1="0" y1="0" x2="1" y2="1">
          <stop offset="0" stop-color="#2fb64b"/>
          <stop offset="1" stop-color="#157a2d"/>
        </linearGradient>
      </defs>
      <polygon points="0,0 380,0 300,210 0,210" fill="url(#band-green)"/>
      <polygon points="0,220 296,220 290,236 0,236" fill="#1f9a3a"/>
      <polygon points="420,0 700,0 700,40 450,40" fill="#1f9a3a"/>
      <polygon points="0,360 700,360 700,400 0,400" fill="#157a2d"/>
      <polygon points="560,360 700,250 700,360" fill="#1f9a3a"/>
    </svg>
    <h2 class="services-heading">
      <span class="word"><span class="initial">S</span>ervices</span>
      <span class="word word--second"><span class="initial">P</span>rovided</span>
    </h2>
    <p class="services-list">
      Real estate and commercial maintenance,
      new home and renovation rewires and upgrades,
      split system air conditioning, floor heat, tv phone data,
      smoke detectors, lighting systems, builders welcome.
    </p>
  </section>

  <section class="card card--front" aria-label="Business card front">
    <span class="brand-square"></span>
    <h1 class="brand-name">
      <span class="line-main">BRIXLEY</span>
      <span class="line-sub">ELECTRICAL</span>
    </h1>
    <div class="brand-rule"></div>
    <p class="tagline">Professional cost effective solutions to all your electrical needs</p>
    <address class="contact">
      <p class="person">Gavin Prestworth</p>
      <p class="licences">[lic no 81926 ac lic no l593721 abn 37216405813]</p>
      <p class="phone">041 735 29 40</p>
      <p class="email">brixleyelectrical@quillnet.com.au</p>
    </address>
  </section>

</main>
</body>
</html>
```